Small Business Consulting Firm Needs Business Card Design

Need a sleek modern business card with 2 sides matching the colors of our logo. We will be placing these with a mailer we are sending out. These business cards will only ever be given to business owners. We operate helping businesses who are struggling with cash flow or finances. If the green and blue design needs to be moved to the right of "Harborline Crest Consulting" for aesthetic purposes that is ok. We will need an editable file if possible. We would like to include the reps name, email, website, and phone number. For now just use Peter Vance, pvance@harborlinecrest.com, www.harborlinecrest.com, and 833-555-0172.

```html
<!DOCTYPE html>
<html lang="en">
<head>
<meta charset="utf-8">
<title>Harborline Crest Consulting – Business Card</title>
<link rel="stylesheet" href="https://fonts.googleapis.com/css2?family=Lato:wght@400;700&display=swap">
<style>
  :root {
    --backdrop: #2b2c2e;
    --card: #1d1e20;
    --card-edge: #262729;
    --ink-light: #d9dadc;
    --ink-muted: #bfc1c4;
    --green: #6cc33b;
    --blue: #1f8fd8;
    --rule: #5a5c60;
    --pattern-a: #202123;
    --pattern-b: #2a2b2e;
  }
  * { box-sizing: border-box; margin: 0; padding: 0; }
  html, body {
    width: 1200px; height: 1108px; overflow: hidden;
    background: var(--backdrop);
    font-family: "Lato", sans-serif;
  }
  .sheet {
    position: relative; width: 1200px; height: 1108px;
    display: flex; justify-content: center; align-items: center; gap: 60px;
  }
  .card {
    position: relative; width: 420px; height: 700px;
    background: var(--card); border-radius: 26px;
    box-shadow: 0 0 0 1px var(--card-edge);
    overflow: hidden;
  }
  /* Front */
  .brand {
    position: absolute; top: 170px; left: 0; right: 0;
    display: flex; flex-direction: column; align-items: center;
  }
  .brand-mark {
    width: 22px; height: 22px; background: var(--green); margin-bottom: 22px;
  }
  .brand-name {
    color: var(--ink-light); font-weight: 400; text-align: center;
    text-transform: uppercase; letter-spacing: 4px; line-height: 1.35;
    font-size: 26px;
  }
  .brand-name span { display: block; font-size: 13px; letter-spacing: 7px; }
  .rep-name {
    position: absolute; top: 440px; left: 0; right: 0; text-align: center;
    font-weight: 700; font-size: 27px; letter-spacing: 0.5px; text-transform: uppercase;
  }
  .rep-name .first { color: var(--green); }
  .rep-name .last { color: var(--blue); }
  .divider {
    position: absolute; top: 490px; left: 60px; right: 60px;
    display: flex; align-items: center; gap: 8px;
  }
  .divider::before, .divider::after {
    content: ""; flex: 1; height: 1px; background: var(--rule);
  }
  .icon {
    width: 26px; height: 26px; border-radius: 50%; background: var(--green);
    display: flex; align-items: center; justify-content: center;
  }
  .icon svg { width: 15px; height: 15px; }
  .contact {
    position: absolute; top: 528px; left: 0; right: 0; text-align: center;
    color: var(--ink-light); font-size: 20px; line-height: 1.4;
  }
  /* Back */
  .back-field {
    position: absolute; inset: 0;
    background: linear-gradient(160deg, var(--pattern-b) 0%, var(--pattern-a) 70%, var(--card) 100%);
  }
  .back-brand {
    position: absolute; top: 440px; left: 0; right: 0;
    display: flex; align-items: center; justify-content: center; gap: 10px;
  }
  .back-brand .brand-mark { margin: 0; width: 16px; height: 16px; }
  .back-brand .brand-name { font-size: 14px; letter-spacing: 3px; }
</style>
</head>
<body>
<main class="sheet">
  <section class="card card-front">
    <div class="brand">
      <div class="brand-mark"></div>
      <div class="brand-name">Harborline Crest<span>Consulting</span></div>
    </div>
    <div class="rep-name"><span class="first">Peter</span> <span class="last">Vance</span></div>
    <div class="divider">
      <div class="icon">
        <svg viewBox="0 0 16 16" fill="none" stroke="#1d1e20" stroke-width="1.8" stroke-linecap="round" stroke-linejoin="round"><path d="M4 2l2 3-1.5 1.5a8 8 0 0 0 5 5L11 10l3 2-1 2.5C7 14 2 9 1.5 3z"/></svg>
      </div>
      <div class="icon">
        <svg viewBox="0 0 16 16" fill="none" stroke="#1d1e20" stroke-width="1.6" stroke-linejoin="round"><rect x="2" y="4" width="12" height="8"/><path d="M2 4l6 5 6-5"/></svg>
      </div>
      <div class="icon">
        <svg viewBox="0 0 16 16" fill="none" stroke="#1d1e20" stroke-width="1.5"><circle cx="8" cy="8" r="6"/><ellipse cx="8" cy="8" rx="2.6" ry="6"/><path d="M2 8h12"/></svg>
      </div>
    </div>
    <div class="contact">
      <p>833-555-0172</p>
      <p>pvance@harborlinecrest.com</p>
      <p>www.harborlinecrest.com</p>
    </div>
  </section>

  <section class="card card-back">
    <div class="back-field" role="img" aria-label="Tonal repeating pattern of the brand symbol in dark grey"></div>
    <div class="back-brand">
      <div class="brand-mark"></div>
      <div class="brand-name">Harborline Crest</div>
    </div>
  </section>
</main>
</body>
</html>
```